Business Card for New Business

Please design a business card using our logo and font files. This is only one card for one person, as listed in details section.

Industry/Entity Type

Business

Contact Information for Business Card

Carl Voserby

Phone 240.318.6624
Cell 703.581.4096
Email carl@moltravex.com

www.moltravex.com

Address
18250 Brennick Lane #314
Harlowe, VA 20715

Font styles to use
Sans Serif

Requirements
Must have
• Information listed in detail section. Must be standard card size.

```html
<!DOCTYPE html>
<html lang="en">
<head>
<meta charset="utf-8">
<title>Moltravex – Business Card</title>
<link href="https://fonts.googleapis.com/css2?family=Quicksand:wght@400&family=Open+Sans:wght@400&display=swap" rel="stylesheet">
<style>
  :root {
    --backdrop: #d9d9d9;
    --card: #ffffff;
    --band: #141414;
    --accent: #e0561c;
    --ink: #1a1a1a;
  }
  html, body {
    margin: 0;
    width: 1200px;
    height: 899px;
    overflow: hidden;
    background: var(--backdrop);
  }
  .card {
    position: absolute;
    left: 360px;
    top: 29px;
    width: 480px;
    height: 840px;
    background: var(--card);
    box-shadow: 0 6px 24px rgba(0,0,0,.18);
  }
  .brand {
    position: absolute;
    left: 0; right: 0;
    top: 0;
    height: 330px;
    display: flex;
    align-items: center;
    justify-content: center;
    gap: 14px;
  }
  .brand-dot {
    width: 44px;
    height: 44px;
    border-radius: 50%;
    background: var(--accent);
  }
  .brand-name {
    font-family: "Quicksand", sans-serif;
    font-weight: 400;
    font-size: 70px;
    letter-spacing: 1px;
    color: var(--accent);
    line-height: 1;
  }
  .name-band {
    position: absolute;
    left: 0; right: 0;
    top: 330px;
    height: 140px;
    background: var(--band);
    display: flex;
    align-items: center;
    justify-content: center;
  }
  .person-name {
    font-family: "Quicksand", sans-serif;
    font-weight: 400;
    font-size: 40px;
    color: var(--accent);
    letter-spacing: .5px;
  }
  .contact-list {
    position: absolute;
    left: 70px;
    top: 530px;
    margin: 0;
    padding: 0;
    list-style: none;
    font-family: "Open Sans", sans-serif;
    font-size: 24px;
    color: var(--ink);
    line-height: 1.6;
  }
  .contact-list li {
    display: flex;
    align-items: flex-start;
    gap: 12px;
  }
  .contact-icon {
    width: 24px;
    height: 24px;
    flex: none;
    margin-top: 8px;
    fill: var(--ink);
  }
  .address { line-height: 1.35; margin-top: 4px; }
</style>
</head>
<body>
  <div class="card">
    <header class="brand">
      <span class="brand-dot"></span>
      <span class="brand-name">moltravex</span>
    </header>

    <div class="name-band">
      <span class="person-name">Carl Voserby</span>
    </div>

    <ul class="contact-list">
      <li>
        <svg class="contact-icon" viewBox="0 0 24 24" aria-hidden="true"><path d="M6.6 2.5l3 3.6-1.9 2.3c1.2 2.7 3.2 4.7 5.9 5.9l2.3-1.9 3.6 3-2 3.6C10.7 18.8 5.2 13.3 3 6.5z"/></svg>
        <span>240.318.6624</span>
      </li>
      <li>
        <svg class="contact-icon" viewBox="0 0 24 24" aria-hidden="true"><path d="M7 1h10a2 2 0 0 1 2 2v18a2 2 0 0 1-2 2H7a2 2 0 0 1-2-2V3a2 2 0 0 1 2-2zm0 3v14h10V4z"/></svg>
        <span>703.581.4096</span>
      </li>
      <li>
        <svg class="contact-icon" viewBox="0 0 24 24" aria-hidden="true"><path d="M2 4h20v16H2zm2 2v.5l8 6 8-6V6zm0 3v9h16V9l-8 6z"/></svg>
        <span>carl@moltravex.com</span>
      </li>
      <li>
        <svg class="contact-icon" viewBox="0 0 24 24" aria-hidden="true"><path d="M2 3h20v14H13v2h4v2H7v-2h4v-2H2zm2 2v10h16V5z"/></svg>
        <span>www.moltravex.com</span>
      </li>
      <li>
        <svg class="contact-icon" viewBox="0 0 24 24" aria-hidden="true"><path d="M12 1a7 7 0 0 1 7 7c0 5-7 15-7 15S5 13 5 8a7 7 0 0 1 7-7zm0 4a3 3 0 1 0 0 6 3 3 0 0 0 0-6z"/></svg>
        <span class="address">18250 Brennick Lane #314<br>Harlowe, VA 20715</span>
      </li>
    </ul>
  </div>
</body>
</html>
```